We need a postcard design for a new promotion. We are an Australian online store that sells craft mosaic supplies, mainly tiles. View our website to understand more about our product range, www.brightlanecrafts.com.au and what we are about.

This promotion is designed to be used with mosaic studios / classes, as a referral system. They will give these cards to their students who will use them when placing an order. They will enter the studios / classes name during the checkout process. The studio will then receive a credit which will entitle them to receive mosaic supplies.

Target Market(s)

Women aged between 30-65, interest in art & craft

Industry/Entity Type

Store

Requirements
Must have
• Logo
Phone number: 1300 684 157
Website URL: www.brightlanecrafts.com.au

The following wording:

You Can Help Stock Your Studio...
Simply place any order with The Pebblecraft Depot and we will give your studio mosaic supplies, to the value of 10% of your purchase.

Just enter your studios name in the comments box during checkout to ensure your studio receives their supplies.

Studio Name:

```html
<!DOCTYPE html>
<html lang="en">
<head>
<meta charset="utf-8">
<title>The Pebblecraft Depot – Studio Referral Postcard</title>
<link href="https://fonts.googleapis.com/css2?family=Roboto+Condensed:wght@400;700&display=swap" rel="stylesheet">
<style>
  :root {
    --backdrop: #4a4a4c;
    --paper: #ffffff;
    --band-pink: #ec3a82;
    --band-blue: #5762b0;
    --badge-pink: #e5067f;
    --badge-orange: #f6a11d;
    --highlight-yellow: #ffe84a;
    --phone-grey: #a09e9c;
    --ink-dark: #333333;
    --url-pink: #e8307d;
  }
  * { margin: 0; padding: 0; box-sizing: border-box; }
  html, body {
    width: 962px; height: 1200px; overflow: hidden;
    background: var(--backdrop);
    font-family: "Roboto Condensed", "Arial Narrow", sans-serif;
  }
  .postcard {
    position: absolute; left: 83px; top: 83px;
    width: 797px; height: 1032px;
    background: var(--paper);
    overflow: hidden;
  }
  .hero-photo {
    position: absolute; left: 0; top: 0; width: 797px; height: 454px;
    background:
      radial-gradient(circle at 105% 110%, #2b4fa8 0 18%, transparent 40%),
      linear-gradient(100deg, #e8412b 0%, #f7862b 16%, #f6d63a 32%, #b7dd6a 45%, #3bb09b 58%, #1f7d86 70%, #7a3a2a 74%, #2f5fb8 82%, #4b6fd0 100%);
  }
  .sale-badge {
    position: absolute; left: 40px; top: 209px;
    width: 220px; height: 220px; border-radius: 50%;
    border: 5px solid var(--paper);
    background: linear-gradient(to bottom, var(--badge-pink) 0 68%, var(--badge-orange) 68% 100%);
    color: var(--paper); font-weight: 700; text-transform: uppercase;
    box-shadow: 0 3px 8px rgba(0,0,0,.35);
  }
  .sale-badge span { position: absolute; left: 44px; line-height: 1; }
  .sale-badge .save { top: 32px; font-size: 46px; }
  .sale-badge .upto { top: 78px; font-size: 18px; }
  .sale-badge .percent { top: 96px; font-size: 60px; letter-spacing: -1px; }
  .sale-badge .percent small { font-size: 30px; }
  .sale-badge .items { top: 162px; left: 40px; font-size: 19px; }
  .offer-band {
    position: absolute; left: 0; top: 454px; width: 797px; height: 305px;
    background: var(--band-pink); color: var(--paper);
    text-align: center; text-transform: uppercase; font-weight: 700;
  }
  .offer-band h1 {
    margin-top: 30px; font-size: 64px; line-height: 70px; letter-spacing: .5px;
  }
  .offer-band p { margin-top: 18px; font-size: 23px; line-height: 32px; }
  .accent { color: var(--highlight-yellow); }
  .instruction-band {
    position: absolute; left: 0; top: 759px; width: 797px; height: 98px;
    background: var(--band-blue); color: var(--paper);
    text-align: center; text-transform: uppercase; font-weight: 700;
    font-size: 19.5px; line-height: 29px; padding-top: 22px;
  }
  .contact { position: absolute; left: 36px; top: 888px; }
  .contact .cta { font-size: 21px; color: var(--ink-dark); text-transform: uppercase; }
  .contact .phone { font-size: 54px; font-weight: 700; color: var(--phone-grey); line-height: 58px; letter-spacing: 1px; }
  .contact .url { font-size: 23px; color: var(--url-pink); }
  .brand-name {
    position: absolute; left: 478px; top: 912px;
    display: flex; align-items: center; gap: 14px;
    color: var(--phone-grey); font-size: 30px; line-height: 32px; text-transform: uppercase;
  }
  .brand-name .mark { width: 44px; height: 44px; background: var(--band-pink); flex: none; }
</style>
</head>
<body>
  <main class="postcard">
    <div class="hero-photo" role="img" aria-label="Close-up photo of colourful glass mosaic tiles laid in curved rainbow rows"></div>
    <div class="sale-badge">
      <span class="save">Save</span>
      <span class="upto">Up to</span>
      <span class="percent">50%<small>on</small></span>
      <span class="items">Sales items</span>
    </div>
    <section class="offer-band">
      <h1>You can help<br>stock your studio...</h1>
      <p>Simply place any order with <span class="accent">The Pebblecraft Depot</span><br>and we will give your studio mosaic supplies, to the<br>value of <span class="accent">10%</span> of your purchase.</p>
    </section>
    <section class="instruction-band">
      Just enter your studios name in the comments box during<br>checkout to ensure your studio receives their supplies.
    </section>
    <div class="contact">
      <div class="cta">Visit now to place your order</div>
      <div class="phone">1300 684 157</div>
      <div class="url">www.brightlanecrafts.com.au</div>
    </div>
    <div class="brand-name"><span class="mark"></span><span>The Pebblecraft<br>Depot</span></div>
  </main>
</body>
</html>
```